Harlow Ridge Gear Pour Chute Product Sticker Design

We are looking to design a sticker (4 inches tall by 6 inches wide) to go on our new tool before we put on the market. the sticker is a basic marketing tool with pictures, descriptions, spot for a bar code, and basic design that sicks out in a work environment. The tool is black and this is going on the back of the tool. Want to look like a cool design, taking into account our logo colors, and something that will pop off a black tool background.

Target Market(s)

This is a specific tool used by masonry and construction workers to put concrete into an existing block wall.

Industry/Entity Type

Masonry

Requirements
Must have
• A clear, simple design that stands out when placed on the back of a black plastic tool. It's for the construction and mason industry, so a more rugged "manly" design is warranted. Have our company design logo in top left corner, clearly see the words "Pour Chute" in middle of sticker, have a few pics of the product, product description and bullet points similar to the pic i attached. Also need a spot in the bottom left for the bar code. On the right please have the following bullets:
• Have a need to get concrete into new masonry openings?
• Save time pouring concrete in existing block walls
• Attaches to wall at the knock out location
• Cut your concrete wall time in half
• As well as the following anywhere else you can fit it:
• Made of polypropylene plastic
• Light weight, durable allowing concrete to flow with ease
• Easy to clean
• MADE IN THE USA!!
• 30-Day Money Back Guarantee!!

```html
<!DOCTYPE html>
<html lang="en">
<head>
<meta charset="UTF-8">
<title>Harlow Ridge Gear – Pour Chute Sticker</title>
<link href="https://fonts.googleapis.com/css2?family=Archivo+Black&family=Archivo+Narrow:wght@700&family=Roboto+Condensed:wght@900&display=swap" rel="stylesheet">
<style>
  :root {
    --backdrop: #141112;
    --red-deep: #7a0a10;
    --red: #c0141c;
    --red-bright: #e3232b;
    --navy: #1b1f5e;
    --navy-band: #12186e;
    --white: #ffffff;
    --photo-grey: #8d9298;
    --product-black: #141414;
  }
  * { box-sizing: border-box; margin: 0; padding: 0; }
  html, body { width: 1200px; height: 1000px; overflow: hidden; background: var(--backdrop); }
  .canvas { position: relative; width: 1200px; height: 1000px; background: var(--backdrop); }

  .sticker {
    position: absolute; left: 165px; top: 198px; width: 875px; height: 582px; overflow: hidden;
    background:
      radial-gradient(ellipse 420px 260px at 640px 170px, rgba(255,255,255,0.75), rgba(255,255,255,0) 70%),
      radial-gradient(ellipse 300px 120px at 200px 200px, rgba(255,255,255,0.45), rgba(255,255,255,0) 75%),
      linear-gradient(180deg, var(--red-deep) 0%, var(--red) 40%, var(--red-bright) 70%, var(--red-deep) 100%);
  }

  .thumb {
    position: absolute; top: 22px; width: 168px; height: 105px;
    border: 4px solid var(--white);
    background: linear-gradient(135deg, #b9bdc2, var(--photo-grey) 60%, #5d6166);
  }
  .thumb--wall { left: 25px; }
  .thumb--blocks { left: 205px; background: linear-gradient(135deg, #7d7a70, #a8a497 55%, #4d4a43); }
  .thumb--mounted { left: 383px; }

  .brand {
    position: absolute; left: 620px; top: 68px; width: 240px;
    font-family: "Archivo Black", sans-serif; font-size: 26px; line-height: 1.05;
    color: var(--navy); text-align: center;
  }

  .product-shot {
    position: absolute; left: 480px; top: 128px; width: 360px; height: 218px;
    border-radius: 14px;
    background: linear-gradient(160deg, #3a3a3a, var(--product-black) 55%, #000);
    box-shadow: 0 0 24px rgba(255,255,255,0.35);
  }

  .title {
    position: absolute; left: 66px; top: 170px;
    font-family: "Archivo Black", sans-serif; font-size: 52px; line-height: 50px;
    letter-spacing: 8px; color: var(--navy);
    text-shadow: 0 0 2px var(--white), 0 0 2px var(--white), 2px 2px 0 var(--white);
  }

  .tagline-band {
    position: absolute; left: 0; top: 280px; width: 620px; height: 68px;
    background: linear-gradient(90deg, var(--navy-band) 0%, var(--navy-band) 75%, rgba(18,24,110,0) 100%);
  }
  .tagline {
    position: absolute; left: 66px; top: 291px;
    font-family: "Archivo Black", sans-serif;
    font-size: 17px; line-height: 22px; letter-spacing: 1.5px; color: var(--white);
  }

  .features { list-style: none; position: absolute; font-family: "Archivo Narrow", sans-serif;
    font-weight: 700; font-size: 14.5px; line-height: 15px; letter-spacing: 1px; color: var(--white); }
  .features li { position: relative; padding-left: 25px; }
  .features li::before {
    content: ""; position: absolute; left: 0; top: 3px; width: 9px; height: 9px;
    background: var(--navy-band); border: 1.5px solid var(--white);
  }
  .features--left { left: 43px; top: 362px; width: 290px; }
  .features--left li { margin-bottom: 10px; }
  .features--left li:nth-child(3) { margin-bottom: 12px; }
  .features--right { left: 365px; top: 360px; width: 270px; }
  .features--right li { margin-bottom: 18px; }

  .made-in {
    position: absolute; left: 69px; top: 534px;
    font-family: "Archivo Narrow", sans-serif; font-weight: 700; font-size: 15px;
    letter-spacing: 2px; color: var(--white);
  }
  .guarantee {
    position: absolute; left: 372px; top: 506px;
    font-family: "Roboto Condensed", sans-serif; font-weight: 900;
    font-size: 20px; line-height: 21px; color: var(--navy);
    text-shadow: 0 0 2px var(--white), 0 0 2px var(--white), 0 0 1px var(--white);
  }
  .barcode-spot {
    position: absolute; left: 646px; top: 470px; width: 205px; height: 90px;
    background: var(--white); display: flex; align-items: center; justify-content: center;
    font-family: "Archivo Narrow", sans-serif; font-size: 19px; letter-spacing: 3px; color: #111;
  }
</style>
</head>
<body>
<div class="canvas">
  <section class="sticker">
    <div class="thumb thumb--wall" role="img" aria-label="Photo of the pour chute attached to a block wall"></div>
    <div class="thumb thumb--blocks" role="img" aria-label="Photo of an open block wall with hollow cells"></div>
    <div class="thumb thumb--mounted" role="img" aria-label="Photo of the pour chute mounted at a knock-out opening"></div>

    <div class="brand">Harlow Ridge Gear</div>

    <div class="product-shot" role="img" aria-label="Photo of the black plastic pour chute"></div>

    <h1 class="title">POUR<br>CHUTE</h1>

    <div class="tagline-band"></div>
    <p class="tagline">Have a need to get concrete into<br>new masonry openings?</p>

    <ul class="features features--left">
      <li>Save time pouring concrete in<br>existing block walls</li>
      <li>Attaches to wall at the knock out<br>location</li>
      <li>Cut your concrete wall time in half</li>
      <li>As well as the following anywhere<br>else you can fit it</li>
    </ul>

    <ul class="features features--right">
      <li>Made of<br>polypropylene plastic</li>
      <li>Light weight, durable allowing<br>concrete to flow with ease</li>
      <li>Easy to clean</li>
    </ul>

    <p class="made-in">MADE IN THE USA</p>
    <p class="guarantee">30-DAY MONEY<br>BACK GUARANTEE!!</p>

    <div class="barcode-spot">BARCODE</div>
  </section>
</div>
</body>
</html>
```